Bramblewick Dill Pickles needs your smart gourmet Design

Looking for a smart design for a dill pickle jar container. The text
Bramblewick Dill Pickles.
Crisp From The Crock.

A tasty reason to raid the refrigerator.

Target Market(s)

Foodies, farmers market types.

Font styles to use
Serif
Sans Serif

Colors

Designer to choose colors to be used in the design.

Requirements
Must have
• Attractive design to entice foodies to buy my Pickles. Not cluttered, easy to read.
Nice to have
• Pickles, garlic. Modern.
Should not have
• Clutter. No script text.

```html
<!DOCTYPE html>
<html lang="en">
<head>
<meta charset="utf-8">
<title>Bramblewick Dill Pickles – Jar Label</title>
<link rel="stylesheet" href="https://fonts.googleapis.com/css2?family=Abril+Fatface&family=Lato:wght@700;900&display=swap">
<style>
  :root {
    --backdrop: #d6b897;
    --label-tan: #c7a685;
    --label-sheen: #d3b493;
    --frame-brown: #3a2120;
    --accent-yellow: #f7b915;
    --text-white: #ffffff;
    --text-dark: #3a1f1a;
    --garlic-cream: #efe6da;
    --parsley-green: #4e8a2c;
  }
  * { box-sizing: border-box; margin: 0; padding: 0; }
  html, body {
    width: 1146px;
    height: 1200px;
    overflow: hidden;
    background: var(--backdrop);
  }
  .canvas {
    position: relative;
    width: 1146px;
    height: 1200px;
    background: var(--backdrop);
  }
  .label {
    position: absolute;
    left: 60px;
    top: 205px;
    width: 1026px;
    height: 790px;
    background: linear-gradient(90deg, var(--label-tan) 0%, var(--label-sheen) 55%, var(--label-tan) 100%);
  }
  .frame {
    position: absolute;
    left: 123px;
    top: 15px;
    width: 780px;
    height: 760px;
  }
  .frame svg { display: block; width: 100%; height: 100%; }
  .frame-content {
    position: absolute;
    inset: 0;
    display: flex;
    flex-direction: column;
    align-items: center;
  }
  .brand-name {
    margin-top: 150px;
    font-family: "Abril Fatface", serif;
    font-size: 92px;
    font-weight: 400;
    line-height: 1;
    color: var(--text-white);
  }
  .product-name {
    margin-top: 16px;
    font-family: "Abril Fatface", serif;
    font-size: 56px;
    line-height: 1;
    color: var(--text-white);
  }
  .tagline {
    margin-top: 12px;
    padding: 4px 20px 2px;
    border-radius: 10px;
    background: var(--accent-yellow);
    font-family: "Lato", sans-serif;
    font-weight: 900;
    font-size: 28px;
    letter-spacing: 1.5px;
    color: var(--text-dark);
    line-height: 1.2;
  }
  .garlic-art {
    margin-top: 22px;
    width: 460px;
    height: 250px;
    border-radius: 48% 48% 40% 40%;
    background:
      radial-gradient(ellipse at 50% 45%, var(--garlic-cream) 0%, #d9c7b3 45%, rgba(217,199,179,0) 70%),
      radial-gradient(ellipse at 15% 70%, var(--parsley-green) 0%, rgba(78,138,44,0) 35%),
      radial-gradient(ellipse at 85% 70%, var(--parsley-green) 0%, rgba(78,138,44,0) 35%);
  }
  .net-weight {
    position: absolute;
    left: 803px;
    top: 700px;
    font-family: "Lato", sans-serif;
    font-weight: 700;
    font-size: 27px;
    line-height: 1.2;
    color: var(--text-dark);
  }
</style>
</head>
<body>
  <main class="canvas">
    <section class="label">
      <div class="frame">
        <svg viewBox="0 0 780 760" aria-hidden="true">
          <path fill="var(--frame-brown)" stroke="var(--accent-yellow)" stroke-width="9" stroke-linejoin="round"
            d="M390,6 C420,34 460,52 520,54 L600,54 C620,54 630,72 640,92 C660,122 690,132 718,132 L718,330 C738,350 756,368 774,380 C756,392 738,410 718,430 L718,628 C690,628 660,638 640,668 C630,688 620,706 600,706 L520,706 C460,708 420,726 390,754 C360,726 320,708 260,706 L180,706 C160,706 150,688 140,668 C120,638 90,628 62,628 L62,430 C42,410 24,392 6,380 C24,368 42,350 62,330 L62,132 C90,132 120,122 140,92 C150,72 160,54 180,54 L260,54 C320,52 360,34 390,6 Z"/>
        </svg>
        <div class="frame-content">
          <h1 class="brand-name">Bramblewick</h1>
          <p class="product-name">Dill Pickles</p>
          <p class="tagline">CRISP FROM THE CROCK</p>
          <div class="garlic-art" role="img" aria-label="Garlic bulbs and cloves with parsley leaves"></div>
        </div>
      </div>
      <p class="net-weight">Nt Wt.<br>50 gm</p>
    </section>
  </main>
</body>
</html>
```